BKA

Please send us some options for letterhead I attached our Logo. In addition to the Logo we need this information somewhere on the page

47 Fenbury Lane
Westport, CT 06880
203-481-7629

```html
<!DOCTYPE html>
<html lang="en">
<head>
<meta charset="utf-8">
<title>BKA Lending Group — Letterhead</title>
<link href="https://fonts.googleapis.com/css2?family=Arimo:wght@400;700&display=swap" rel="stylesheet">
<style>
  :root {
    --backdrop: #e9e7e4;
    --paper: #ffffff;
    --brand-brown: #4b3f3b;
    --brand-blue: #1e8fd6;
    --rule-grey: #8a8786;
    --mark-grey: rgba(226, 224, 224, 0.55);
    --mark-blue: rgba(205, 226, 243, 0.55);
  }
  * { box-sizing: border-box; margin: 0; padding: 0; }
  html, body {
    width: 1200px;
    height: 1200px;
    overflow: hidden;
    background: var(--backdrop);
  }
  .letterhead {
    position: absolute;
    left: 175px;
    top: 50px;
    width: 850px;
    height: 1100px;
    background: var(--paper);
    box-shadow: 0 6px 24px rgba(0,0,0,0.12);
    overflow: hidden;
    font-family: "Arimo", Arial, sans-serif;
  }
  .letterhead__brand {
    position: absolute;
    top: 92px;
    left: 0;
    right: 0;
    display: flex;
    justify-content: center;
    align-items: center;
    gap: 12px;
    z-index: 1;
  }
  .brand__square {
    width: 30px;
    height: 30px;
    background: var(--brand-blue);
  }
  .brand__name {
    font-size: 26px;
    font-weight: 700;
    color: var(--brand-brown);
    letter-spacing: 0.4px;
  }
  .letterhead__watermark {
    position: absolute;
    left: -80px;
    top: 240px;
    width: 760px;
    height: 700px;
    background:
      radial-gradient(ellipse 55% 35% at 40% 85%, var(--mark-blue) 0%, rgba(255,255,255,0) 100%),
      radial-gradient(ellipse 50% 50% at 45% 45%, var(--mark-grey) 0%, rgba(255,255,255,0) 100%);
  }
  .letterhead__footer {
    position: absolute;
    bottom: 62px;
    left: 0;
    right: 0;
    display: flex;
    justify-content: center;
    align-items: center;
    gap: 14px;
    z-index: 1;
  }
  .footer__rule {
    width: 40px;
    height: 2px;
    background: var(--rule-grey);
  }
  .footer__contact {
    font-size: 13px;
    color: var(--brand-blue);
    letter-spacing: 0.2px;
  }
</style>
</head>
<body>
  <main class="letterhead">
    <header class="letterhead__brand">
      <span class="brand__square"></span>
      <span class="brand__name">BKA Lending Group</span>
    </header>

    <div class="letterhead__watermark" role="img" aria-label="Faint large brand symbol decoration in soft grey and light blue"></div>

    <footer class="letterhead__footer">
      <span class="footer__rule"></span>
      <p class="footer__contact">47 Fenbury Lane • Westport, CT 06880 • 203-481-7629</p>
      <span class="footer__rule"></span>
    </footer>
  </main>
</body>
</html>
```